I need 4 Power Point foils for 4 companies.
1 Folis for Tovanta, 1 Foils for Luxury, 1 Folis for Hospitality Group and the mother of Tovan and Luxury is Hospitality. So we also need a foil as head hospitality and you have to realize that the other companies belong to it. I would like a cover sheet and a presentation templates.
Updates
Hey i Need for My companies Presentation Cover and Template thank you
Target Market(s)
Travel industry
Colors
Designer to choose only greyscale colors for use in the design.
Requirements
Must have
- create your own design

```html
<!DOCTYPE html>
<html lang="en">
<head>
<meta charset="utf-8">
<title>Havenmere Group – Presentation Template</title>
<link href="https://fonts.googleapis.com/css2?family=Oswald:wght@500&family=Roboto:wght@300;400;500&display=swap" rel="stylesheet">
<style>
:root{
  --ink:#55595c;
  --text:#333;
  --muted:#8a8a8a;
  --dark:#222;
  --sky:linear-gradient(180deg,#d6d6d6 0%,#c4c4c4 35%,#efefef 60%,#8e8e8e 100%);
  --pool:linear-gradient(180deg,#3a3a3a 0%,#d0d0d0 35%,#bdbdbd 55%,#7a7a7a 75%,#555 100%);
  --room:linear-gradient(160deg,#eeeeee 0%,#b0b0b0 45%,#4a4a4a 100%);
  --arch:linear-gradient(170deg,#f6f6f6 0%,#c6c6c6 40%,#353535 100%);
  --garden:linear-gradient(170deg,#e4e4e4,#7c7c7c 40%,#9a9a9a 70%,#e2e2e2);
  --villa:linear-gradient(170deg,#e0e0e0,#8a8a8a 50%,#ececec);
  --road:linear-gradient(180deg,#a8a8a8,#c8c8c8 55%,#3a3a3a);
  --lobby:linear-gradient(180deg,#1c1c1c,#7a7a7a 55%,#2a2a2a);
  --lounge:linear-gradient(160deg,#dadada,#a6a6a6 50%,#4e4e4e);
}
*{margin:0;padding:0;box-sizing:border-box}
html,body{width:1200px;height:2194px;overflow:hidden;background:#fff}
.page{width:1422px;height:2600px;transform:scale(.84388);transform-origin:0 0;position:relative;font-family:'Roboto',sans-serif;color:var(--text)}
.brand{position:absolute;left:128px;top:71px;width:244px;height:244px;border:5px solid var(--ink);border-radius:50%;display:flex;align-items:center;justify-content:center;text-align:center;font-size:30px;font-weight:500;color:var(--ink);line-height:1.15}
.sheet-title{position:absolute;left:470px;top:124px;font-family:'Oswald',sans-serif;font-weight:500;font-size:88px;letter-spacing:7px;color:var(--ink);line-height:1;white-space:nowrap}
.slide{position:absolute;width:566px;height:318px;overflow:hidden;background:#fff;box-shadow:4px 12px 28px rgba(0,0,0,.35)}
.col-l{left:86px}.col-r{left:760px}
.r1{top:424px}.r2{top:828px}.r3{top:1232px}.r4{top:1636px}.r5{top:2040px}
.grey{background:linear-gradient(160deg,#fafafa 0%,#e0e0e0 45%,#b3b3b3 100%)}
.photo{position:absolute}
.round{border-radius:50%}
.foot{position:absolute;bottom:7px;left:40px;font-size:5px;color:var(--muted)}
.pg{position:absolute;bottom:7px;right:32px;font-size:5px;color:var(--muted)}
.mark{position:absolute;top:16px;right:34px;width:42px;height:42px;border:1.5px solid var(--ink);border-radius:50%;display:flex;align-items:center;justify-content:center;text-align:center;font-size:6.5px;font-weight:500;color:var(--ink);line-height:1.1}
h2{font-weight:400;color:#333;position:absolute;line-height:1.05}
p{font-weight:300}
.cover .glow{position:absolute;left:-160px;top:-200px;width:560px;height:560px;border-radius:50%;background:rgba(235,235,235,.55)}
.cover .glow2{left:-130px;top:-170px;width:500px;height:500px;background:rgba(225,225,225,.6)}
.cover .base{position:absolute;left:0;bottom:0;width:420px;height:200px;background:linear-gradient(0deg,#e6e6e6,rgba(255,255,255,0))}
.cover .pic{left:-110px;top:-175px;width:420px;height:420px;background:var(--sky)}
.cover .name{position:absolute;left:370px;top:50px;width:120px;height:120px;border:2px solid var(--ink);border-radius:50%;display:flex;align-items:center;justify-content:center;font-size:14px;font-weight:500;color:var(--ink);text-align:center}
.cover h2{left:290px;width:252px;top:183px;font-size:20px;text-align:center}
.cover .rule{position:absolute;left:290px;width:252px;top:238px;height:1px;background:#ccc}
.cover .sub{position:absolute;left:290px;width:252px;top:246px;text-align:center;font-size:11px;letter-spacing:2px;color:#666;font-weight:300}
.toc .pic{left:-160px;top:-150px;width:420px;height:420px;background:var(--pool)}
.toc h2{left:313px;top:30px;font-size:22px}
.toc ol{list-style:none;position:absolute;left:326px;top:66px}
.toc li{display:flex;align-items:center;height:34px;font-size:12px;color:#555;font-weight:300;letter-spacing:.4px}
.toc .num{width:19px;height:19px;border-radius:50%;background:var(--dark);color:#fff;font-size:10px;display:flex;align-items:center;justify-content:center;margin-right:29px}
.welcome .pic{left:355px;top:0;width:211px;height:318px;background:var(--arch)}
.welcome h2{left:44px;top:72px;font-size:21px}
.welcome p{position:absolute;left:41px;top:110px;width:207px;font-size:7.6px;line-height:1.55;color:#666;text-align:justify}
.welcome .badge{position:absolute;left:272px;top:82px;width:164px;height:164px;border-radius:50%;background:radial-gradient(circle at 40% 35%,#e2e2e2,#a8a8a8);box-shadow:0 6px 14px rgba(0,0,0,.3);display:flex;align-items:center;justify-content:center;font-size:15px;font-weight:500;color:var(--ink);text-align:center}
.about .pic{left:-170px;top:-190px;width:430px;height:430px;background:var(--sky)}
.about .pic2{left:40px;top:65px;width:205px;height:205px;background:linear-gradient(180deg,#d2d2d2,#c8c8c8 40%,#efefef 60%,#7e7e7e);box-shadow:0 6px 14px rgba(0,0,0,.35)}
.about h2{left:300px;top:72px;font-size:22px}
.about p{position:absolute;left:300px;top:150px;width:174px;font-size:7.8px;line-height:1.95;color:#555;text-align:justify}
.band{position:absolute;left:0;top:0;width:100%;background:linear-gradient(180deg,#f0f0f0,#b0b0b0)}
.centre-title{left:0;width:100%;text-align:center;font-size:22px;color:#555}
.dot{position:absolute;border-radius:50%;box-shadow:0 2px 5px rgba(0,0,0,.35)}
.dest .dot{width:68px;height:68px}
.cap{position:absolute;width:120px;text-align:center}
.cap b{display:block;font-size:7px;font-weight:500;color:#aaa}
.cap i{display:block;font-style:normal;font-size:5.5px;color:#555;margin-top:3px}
.serv .dot{width:94px;height:94px}
.serv .item{position:absolute;top:184px;width:92px}
.serv .item strong{display:block;font-size:10px;font-weight:300;color:#777}
.serv .item p{font-size:4.6px;line-height:1.7;color:#777;text-align:justify;margin-top:6px}
.amen .pic{left:-140px;top:-145px;width:355px;height:355px;background:var(--room)}
.amen .pic2{left:429px;top:174px;width:150px;height:150px;background:var(--garden)}
.amen h2{left:242px;top:20px;font-size:26px;color:#555}
.amen p{position:absolute;left:240px;top:66px;width:186px;font-size:8.4px;line-height:1.5;color:#333;text-align:justify}
.bul .pic{left:-200px;top:-60px;width:410px;height:440px;background:var(--pool)}
.bul h2{left:243px;top:20px;font-size:23px;color:#222}
.bul ul{list-style:none;position:absolute;left:240px;top:68px;width:290px}
.bul li{display:flex;align-items:center;height:38px;font-size:5.3px;line-height:1.8;color:#555}
.bul svg{flex:none;margin-right:10px}
.pack .pic{left:0;top:0;width:290px;height:318px;background:linear-gradient(170deg,#e6e6e6,#9a9a9a 35%,#bcbcbc 60%,#6a6a6a 85%);clip-path:polygon(0 0,120px 0,285px 318px,0 318px)}
.pack h2{left:172px;top:24px;font-size:21px}
.pack p{position:absolute;font-size:5.1px;line-height:1.95;color:#7a7a7a;text-align:justify}
.pack .p1{left:208px;top:100px;width:330px}
.pack .p2{left:304px;top:154px;width:234px}
.cont .name{position:absolute;left:72px;top:26px;width:80px;height:80px;border:1.5px solid var(--ink);border-radius:50%;display:flex;align-items:center;justify-content:center;font-size:10px;font-weight:500;color:var(--ink);text-align:center}
.cont h2{left:48px;top:124px;font-size:29px;color:#555}
.cont .info{position:absolute;width:110px}
.cont .info strong{display:block;font-size:7px;font-weight:500;color:#666;letter-spacing:.6px}
.cont .info span{display:block;font-size:4.6px;color:#777;line-height:1.9;margin-top:3px}
.cont .pic{left:302px;top:58px;width:216px;height:216px;background:linear-gradient(150deg,#f4f4f4,#c2c2c2 45%,#6e6e6e 70%,#333);box-shadow:0 4px 10px rgba(0,0,0,.3);border:3px solid #fff}
.cont .half{position:absolute;left:505px;top:140px;width:40px;height:60px;border-radius:0 30px 30px 0 / 0 30px 30px 0;background:#bdbdbd;clip-path:inset(0 0 0 50%)}
</style>
</head>
<body>
<div class="page">
  <div class="brand">Havenmere<br>Group</div>
  <div class="sheet-title">POWERPOINT TEMPLATE</div>

  <section class="slide cover col-l r1">
    <div class="base"></div>
    <div class="glow"></div>
    <div class="glow glow2"></div>
    <div class="photo round pic" role="img" aria-label="Traveller seated on a rock above a sea of clouds at sunrise"></div>
    <div class="name">Havenmere<br>Group</div>
    <h2>Your can place the presentation title here</h2>
    <div class="rule"></div>
    <div class="sub">Your master subtitle here</div>
  </section>

  <section class="slide toc col-r r1">
    <div class="photo round pic" role="img" aria-label="Infinity pool overlooking a coastal town at sunset"></div>
    <svg class="photo" style="left:0;top:0" width="566" height="318" aria-hidden="true">
      <circle cx="50" cy="60" r="214" fill="none" stroke="#444" stroke-width=".8"/>
      <circle cx="55" cy="62" r="210" fill="none" stroke="#999" stroke-width=".8"/>
      <circle cx="58" cy="58" r="216" fill="none" stroke="#666" stroke-width=".8"/>
    </svg>
    <h2>Table of content</h2>
    <ol>
      <li><span class="num">1.</span>About Luxury</li>
      <li><span class="num">2.</span>What We do</li>
      <li><span class="num">3.</span>Our Team</li>
      <li><span class="num">4.</span>Our Services</li>
      <li><span class="num">5.</span>Our destinations</li>
      <li><span class="num">6.</span>Our Packages</li>
      <li><span class="num">7.</span>Contact</li>
    </ol>
    <div class="foot">www.havenmeregroup.com</div><div class="pg">page &nbsp; 2</div>
  </section>

  <section class="slide welcome col-l r2">
    <div class="photo pic" role="img" aria-label="White arched riad courtyard with curtains and lounge chairs"></div>
    <div class="badge">Havenmere<br>Group</div>
    <h2>Welcome Message</h2>
    <p>Sed ut perspiciatis unde omnis iste natus error sit voluptatem accusantium doloremque laudantium, totam rem aperiam, eaque ipsa quae ab illo inventore veritatis et quasi architecto beatae vitae dicta sunt explicabo. Nemo enim ipsam voluptatem quia voluptas sit aspernatur aut odit aut fugit, sed quia consequuntur magni dolores eos qui ratione voluptatem sequi nesciunt. Neque porro quisquam est, qui dolorem ipsum quia dolor sit amet, consectetur, adipisci velit, sed quia non numquam eius modi</p>
    <div class="foot">www.havenmeregroup.com</div>
  </section>

  <section class="slide about grey col-r r2">
    <div class="photo round pic" role="img" aria-label="Sunrise sky above a sea of clouds"></div>
    <div class="photo round pic2" role="img" aria-label="Traveller seated on a rock above the clouds"></div>
    <div class="mark">Havenmere</div>
    <h2>About<br>Havenmere<br>Group</h2>
    <p>Sed ut perspiciatis unde omnis iste natus error sit voluptatem accusantium doloremque laudantium, totam rem aperiam, eaque ipsa quae ab illo inventore veritatis et quasi architecto beatae vitae dicta sunt explicabo. Nemo enim ipsam voluptatem quia voluptas sit aspernatur aut odit aut fugit, sed quia consequuntur</p>
    <div class="foot">www.havenmeregroup.com</div><div class="pg">page &nbsp; 4</div>
  </section>

  <section class="slide dest col-l r3">
    <div class="band" style="height:112px"></div>
    <div class="mark">Havenmere</div>
    <h2 class="centre-title" style="top:26px">Our destinations</h2>
    <div class="dot" style="left:39px;top:75px;background:var(--sky)" role="img" aria-label="Clouds at sunrise"></div>
    <div class="dot" style="left:179px;top:75px;background:var(--arch)" role="img" aria-label="Riad courtyard"></div>
    <div class="dot" style="left:319px;top:75px;background:var(--pool)" role="img" aria-label="Infinity pool at sunset"></div>
    <div class="dot" style="left:460px;top:75px;background:var(--villa)" role="img" aria-label="Resort villa with palms"></div>
    <div class="dot" style="left:39px;top:186px;background:var(--garden)" role="img" aria-label="Garden terrace breakfast"></div>
    <div class="dot" style="left:179px;top:186px;background:var(--room)" role="img" aria-label="Hotel dining room"></div>
    <div class="dot" style="left:319px;top:186px;background:var(--road)" role="img" aria-label="Desert road under open sky"></div>
    <div class="dot" style="left:460px;top:186px;background:var(--lobby)" role="img" aria-label="Dark hotel lobby"></div>
    <div class="cap" style="left:13px;top:151px"><b>Title site information</b><i>Country state</i></div>
    <div class="cap" style="left:153px;top:151px"><b>Title site information</b><i>Country state</i></div>
    <div class="cap" style="left:293px;top:151px"><b>Title site information</b><i>Country state</i></div>
    <div class="cap" style="left:434px;top:151px"><b>Title site information</b><i>Country state</i></div>
    <div class="cap" style="left:13px;top:262px"><b>Title site information</b><i>Country state</i></div>
    <div class="cap" style="left:153px;top:262px"><b>Title site information</b><i>Country state</i></div>
    <div class="cap" style="left:293px;top:262px"><b>Title site information</b><i>Country state</i></div>
    <div class="cap" style="left:434px;top:262px"><b>Title site information</b><i>Country state</i></div>
    <div class="foot">www.havenmeregroup.com</div><div class="pg">page &nbsp; 5</div>
  </section>

  <section class="slide serv col-r r3">
    <div class="band" style="height:136px"></div>
    <div class="mark">Havenmere</div>
    <h2 class="centre-title" style="top:22px">Our services</h2>
    <div class="dot" style="left:43px;top:86px;background:var(--lounge)" role="img" aria-label="Airport lounge with plane at sunset"></div>
    <div class="dot" style="left:175px;top:86px;background:var(--arch)" role="img" aria-label="Riad courtyard"></div>
    <div class="dot" style="left:306px;top:86px;background:var(--room)" role="img" aria-label="Hotel dining room"></div>
    <div class="dot" style="left:438px;top:86px;background:var(--garden)" role="img" aria-label="Garden terrace breakfast"></div>
    <div class="item" style="left:43px"><strong>Your service 02</strong><p>Sed ut perspiciatis unde omnis iste natus error sit voluptatem accusantium doloremque laudantium, totam rem aperiam, eaque ipsa quae ab illo inventore veritatis et quasi architecto beatae vitae dicta sunt explicabo.</p></div>
    <div class="item" style="left:178px"><strong>Your service 02</strong><p>Sed ut perspiciatis unde omnis iste natus error sit voluptatem accusantium doloremque laudantium, totam rem aperiam, eaque ipsa quae ab illo inventore veritatis et quasi architecto beatae vitae dicta sunt explicabo.</p></div>
    <div class="item" style="left:309px"><strong>Your service 02</strong><p>Sed ut perspiciatis unde omnis iste natus error sit voluptatem accusantium doloremque laudantium, totam rem aperiam, eaque ipsa quae ab illo inventore veritatis et quasi architecto beatae vitae dicta sunt explicabo.</p></div>
    <div class="item" style="left:444px"><strong>Your service 02</strong><p>Sed ut perspiciatis unde omnis iste natus error sit voluptatem accusantium doloremque laudantium, totam rem aperiam, eaque ipsa quae ab illo inventore veritatis et quasi architecto beatae vitae dicta sunt explicabo.</p></div>
    <div class="foot">www.havenmeregroup.com</div><div class="pg">page &nbsp; 6</div>
  </section>

  <section class="slide amen grey col-l r4">
    <div class="photo round pic" role="img" aria-label="Elegant hotel dining room with long curtains"></div>
    <div class="photo round pic2" role="img" aria-label="Garden terrace with breakfast table"></div>
    <div class="mark">Havenmere</div>
    <h2>Amenities</h2>
    <p>No ceteros verterem his, sea eius iisque eu. Et vis stet dolorem perpetua, usu ea diam affert labores. No ceteros verterem his, sea eius iisque eu. Et vis stet dolorem perpetua, usu ea diam affert labores. No ceteros verterem his, sea eius iisque eu. Et vis stet dolorem perpetua, usu ea diam affert labores. No ceteros verterem his, sea eius iisque eu. Et vis stet dolorem perpetua, usu ea diam affert labores. No ceteros verterem his, sea eius iisque eu. Et vis stet dolorem perpetua, usu ea diam affert labores. No ceteros verterem his, sea eius iisque eu. Et vis stet dolorem perpetua, usu ea diam affert labores.</p>
    <div class="foot">www.havenmeregroup.com</div>
  </section>

  <section class="slide bul grey col-r r4">
    <div class="photo pic round" role="img" aria-label="Infinity pool overlooking a coastal town at dusk"></div>
    <div class="mark">Havenmere</div>
    <h2>Bullets options slide</h2>
    <ul>
      <li><svg width="13" height="13" viewBox="0 0 13 13"><circle cx="6.5" cy="6.5" r="5.8" fill="none" stroke="#666" stroke-width=".8"/><path d="M3.8 6.7l2 2 3.6-4" fill="none" stroke="#666" stroke-width=".9"/></svg>A presentation template created with attentive detail to provide a new experience for users. Hopefully this presentation can help you and bring.</li>
      <li><svg width="13" height="13" viewBox="0 0 13 13"><circle cx="6.5" cy="6.5" r="5.8" fill="none" stroke="#666" stroke-width=".8"/><path d="M3.8 6.7l2 2 3.6-4" fill="none" stroke="#666" stroke-width=".9"/></svg>A presentation template created with attentive detail to provide a new experience for users. Hopefully this presentation can help you and bring.</li>
      <li><svg width="13" height="13" viewBox="0 0 13 13"><circle cx="6.5" cy="6.5" r="5.8" fill="none" stroke="#666" stroke-width=".8"/><path d="M3.8 6.7l2 2 3.6-4" fill="none" stroke="#666" stroke-width=".9"/></svg>A presentation template created with attentive detail to provide a new experience for users. Hopefully this presentation can help you and bring.</li>
      <li><svg width="13" height="13" viewBox="0 0 13 13"><circle cx="6.5" cy="6.5" r="5.8" fill="none" stroke="#666" stroke-width=".8"/><path d="M3.8 6.7l2 2 3.6-4" fill="none" stroke="#666" stroke-width=".9"/></svg>A presentation template created with attentive detail to provide a new experience for users. Hopefully this presentation can help you and bring.</li>
      <li><svg width="13" height="13" viewBox="0 0 13 13"><circle cx="6.5" cy="6.5" r="5.8" fill="none" stroke="#666" stroke-width=".8"/><path d="M3.8 6.7l2 2 3.6-4" fill="none" stroke="#666" stroke-width=".9"/></svg>A presentation template created with attentive detail to provide a new experience for users. Hopefully this presentation can help you and bring.</li>
      <li><svg width="13" height="13" viewBox="0 0 13 13"><circle cx="6.5" cy="6.5" r="5.8" fill="none" stroke="#666" stroke-width=".8"/><path d="M3.8 6.7l2 2 3.6-4" fill="none" stroke="#666" stroke-width=".9"/></svg>A presentation template created with attentive detail to provide a new experience for users. Hopefully this presentation can help you and bring.</li>
    </ul>
    <div class="pg">page</div>
  </section>

  <section class="slide pack col-l r5">
    <div class="photo pic" role="img" aria-label="Tropical resort pool with thatched villa and palms"></div>
    <div class="mark">Havenmere</div>
    <h2>Our Packages</h2>
    <p class="p1">Sed ut perspiciatis unde omnis iste natus error sit voluptatem accusantium doloremque laudantium, totam rem aperiam, eaque ipsa quae ab illo inventore veritatis et quasi architecto beatae vitae dicta sunt explicabo. Nemo enim ipsam voluptatem quia voluptas sit aspernatur aut odit. Sed ut perspiciatis unde omnis iste natus error sit voluptatem accusantium doloremque laudantium, totam</p>
    <p class="p2">Sed ut perspiciatis unde omnis iste natus error sit voluptatem accusantium dNo ceteros verterem his, sea eius iisque eu. Et vis stet dolorem perpetua, usu ea diam affert labores. No ceteros verterem his, sea eius iisque eu. Et vis stet dolorem perpetua, usu ea diam affert labores. No ceteros verterem his, sea eius iisque eu. Et vis stet dolorem perpetua, usu ea diam affert labores. No ceteros verterem his, sea eius iisque eu. Et vis stet dolorem perpetua, usu ea diam affert labores. No ceteros verterem his, sea eius iisque eu. Et vis stet dolorem perpetua, usu ea diam affert labores.</p>
    <div class="pg">page</div>
  </section>

  <section class="slide cont grey col-r r5">
    <div class="name">Havenmere<br>Group</div>
    <h2>Contact</h2>
    <div class="info" style="left:48px;top:166px"><strong>OFFICE HOURS</strong><span>Monday – Thursday<br>08:00 – 17:00</span></div>
    <div class="info" style="left:159px;top:166px"><strong>OUR ADDRESS</strong><span>1224 Lorem imp sum Parkway<br>Lorem View, CA 123-456<br>United States</span></div>
    <div class="info" style="left:48px;top:232px"><strong>GET IN TOUCH</strong><span>(+1) 555-123 456 700<br>(+1) 555-123 456 789<br>(+1) 555-123 456 780</span></div>
    <div class="info" style="left:159px;top:232px"><strong>FOLLOW US</strong><span>@tovanta<br>www.tovanta.com<br>office@tovanta.com</span></div>
    <div class="photo round pic" role="img" aria-label="Hands typing on a laptop keyboard"></div>
    <div class="half"></div>
    <div class="foot">www.havenmeregroup.com</div><div class="pg">page</div>
  </section>
</div>
</body>
</html>
```